Letterhead Creation

I would like to create a letterhead incorporating my family crest attached. My current letterhead with my information is also attached. I would also like to add my Paralegal Marisol Dunleavy

```html
<!DOCTYPE html>
<html lang="en">
<head>
<meta charset="utf-8">
<title>Law Offices of Graham T. Wexley — Letterhead</title>
<link rel="stylesheet" href="https://fonts.googleapis.com/css2?family=Josefin+Sans:wght@300;400&family=Questrial&family=Open+Sans:ital,wght@1,700&display=swap">
<style>
  :root {
    --backdrop: #e4e5e7;
    --paper: #f2f2f3;
    --header-slate: #4c6779;
    --header-indigo: #5b6c9c;
    --header-accent: #8391c1;
    --footer-blue: #3159a6;
    --footer-deep: #1e2f40;
    --mark-blue: #2c4a9a;
    --faint-mark: #e2e3ea;
    --ink-light: #ffffff;
  }
  * { margin: 0; padding: 0; box-sizing: border-box; }
  html, body {
    width: 1200px; height: 1000px; overflow: hidden;
    background: var(--backdrop);
  }
  .canvas {
    width: 1200px; height: 1000px;
    display: flex; align-items: center; justify-content: center;
  }
  .letterhead {
    position: relative;
    width: 728px; height: 940px;
    background: var(--paper);
    box-shadow: 0 10px 30px rgba(0,0,0,0.15);
    overflow: hidden;
  }
  .letterhead-shapes { position: absolute; inset: 0; }
  .firm-mark {
    position: absolute; left: 34px; top: 18px;
    display: flex; align-items: center; gap: 6px;
  }
  .firm-mark-square {
    width: 22px; height: 22px; background: var(--mark-blue);
  }
  .firm-mark-name {
    font-family: "Josefin Sans", sans-serif; font-weight: 400;
    font-size: 15px; color: var(--ink-light); letter-spacing: 1px;
  }
  .firm-title {
    position: absolute; left: 210px; top: 24px;
    font-family: "Josefin Sans", sans-serif; font-weight: 300;
    font-size: 23px; letter-spacing: 2px; text-transform: uppercase;
    color: var(--ink-light);
  }
  .faint-mark {
    position: absolute; right: -10px; top: 520px;
    font-family: "Josefin Sans", sans-serif; font-weight: 400;
    font-size: 84px; letter-spacing: 4px; text-transform: uppercase;
    color: var(--faint-mark);
  }
  .contact-block {
    position: absolute; right: 24px; top: 796px;
    font-family: "Questrial", sans-serif; font-style: normal; font-size: 12.5px;
    color: var(--ink-light); text-align: right;
  }
  .contact-row {
    display: flex; justify-content: flex-end; align-items: center;
    gap: 18px; margin-bottom: 8px; line-height: 1.35;
  }
  .contact-row svg { width: 13px; height: 13px; flex: none; fill: var(--ink-light); }
  .paralegal {
    font-family: "Open Sans", sans-serif; font-style: italic; font-weight: 700;
    font-size: 12px; margin-top: 2px; padding-right: 31px;
  }
</style>
</head>
<body>
<main class="canvas">
  <article class="letterhead">
    <svg class="letterhead-shapes" viewBox="0 0 728 940" width="728" height="940" aria-hidden="true">
      <defs>
        <linearGradient id="header-fill" x1="0" x2="1" y1="0" y2="0">
          <stop offset="0" stop-color="#4c6779"/>
          <stop offset="1" stop-color="#5b6c9c"/>
        </linearGradient>
        <linearGradient id="footer-fill" x1="0" x2="1" y1="0" y2="0">
          <stop offset="0" stop-color="#3159a6"/>
          <stop offset="0.5" stop-color="#3159a6"/>
          <stop offset="1" stop-color="#1e2f40"/>
        </linearGradient>
      </defs>
      <path class="header-accent" d="M0 62 Q360 70 728 62 V112 Q520 82 0 70 Z" fill="#8391c1"/>
      <path class="header-band" d="M0 0 H728 V70 Q420 64 0 66 Z" fill="url(#header-fill)"/>
      <path class="footer-wave" d="M0 680 C140 690 250 845 380 842 C520 838 640 760 728 700 V940 H0 Z" fill="url(#footer-fill)"/>
    </svg>

    <div class="firm-mark">
      <span class="firm-mark-square"></span>
      <span class="firm-mark-name">Wexley</span>
    </div>
    <h1 class="firm-title">Law Offices of Graham T. Wexley</h1>
    <div class="faint-mark">Wexley</div>

    <address class="contact-block">
      <div class="contact-row"><span>(555)0148217</span>
        <svg viewBox="0 0 24 24"><path d="M6.6 10.8a15 15 0 0 0 6.6 6.6l2.2-2.2a1 1 0 0 1 1-.25 11.4 11.4 0 0 0 3.6.57 1 1 0 0 1 1 1V20a1 1 0 0 1-1 1A17 17 0 0 1 3 4a1 1 0 0 1 1-1h3.5a1 1 0 0 1 1 1c0 1.25.2 2.45.57 3.57a1 1 0 0 1-.25 1z"/></svg></div>
      <div class="contact-row"><span>(555)0193604</span>
        <svg viewBox="0 0 24 24"><path d="M7 3h8v5H7z M4 9h16v12H4z M8 12h2v2H8z M12 12h2v2h-2z M8 16h2v2H8z M12 16h2v2h-2z" fill-rule="evenodd"/></svg></div>
      <div class="contact-row"><span>graham@wexleylawpc.com</span>
        <svg viewBox="0 0 24 24"><path d="M2 5h20v14H2z M4 7v.5l8 5.5 8-5.5V7z M4 9.9V17h16V9.9l-8 5.5z" fill-rule="evenodd"/></svg></div>
      <div class="contact-row"><span>Harlow, Ca 91806<br>412 N. Alder Ave.</span>
        <svg viewBox="0 0 24 24"><path d="M12 2a7 7 0 0 0-7 7c0 5 7 13 7 13s7-8 7-13a7 7 0 0 0-7-7zm0 9.5A2.5 2.5 0 1 1 12 6.5a2.5 2.5 0 0 1 0 5z"/></svg></div>
      <div class="paralegal">Paralegal: Marisol Dunleavy</div>
    </address>
  </article>
</main>
</body>
</html>
```